[WEB DESIGN - Start-up] Online LOANS against Luxury Assets - Needs a Web Design

Hello,
We need a web design for a new company. We make online LOANS against Luxury assets.
The name is private, that's why you could remplace it by the term "LOGO" or "ENTERPRISE".

In attachments, you'll find few models that we would like. Nonetheless, we don't want a copy of these screenshots. They are only prototypes that we made. Here we expect you to lead a professional web Design with your intuition and your ideas.

The final design should communicate start-up spirit, professionalism and fluidity.

Best Regards.

Industry/Entity Type

Finance

Number of Pages Required

2 page

Font styles to use
Sans Serif

Colors
f78f20
ffffff
b2b2b2
e9e9e9

Requirements
Must have
• The designer will draw on the 2015 web trends.
• The subject site is serious (loans against luxury assets), but the site should be modern and pleasant.
• PLEASE REFER YOU TO MY MODEL ( ATTACHMENTS)
Nice to have
• Surprise-me ! Welcome to a lot of imagination.

```html
<!DOCTYPE html>
<html lang="fr">
<head>
<meta charset="utf-8">
<title>VALORA – Prêts sur objets de luxe</title>
<link href="https://fonts.googleapis.com/css2?family=Oswald:wght@400;600;700&family=Open+Sans:wght@400;600;700&display=swap" rel="stylesheet">
<style>
:root{
  --orange:#f78f20;
  --orange-dark:#c9670c;
  --white:#ffffff;
  --grey:#b2b2b2;
  --light:#e9e9e9;
  --text:#6d6d6d;
  --dark:#1f1f1f;
}
*{margin:0;padding:0;box-sizing:border-box}
html,body{width:859px;height:1200px;overflow:hidden;background:var(--white);font-family:"Open Sans",sans-serif;color:var(--text)}
.page{position:relative;width:859px;height:1200px}

/* hero */
.hero{position:absolute;left:0;top:0;width:859px;height:235px;overflow:hidden}
.hero-photo{position:absolute;inset:0;background:radial-gradient(ellipse at 60% 40%,#f6a64a 0%,#d77a1c 35%,#6a3a10 70%,#2a1a0c 100%)}
.site-header{position:absolute;left:0;top:0;width:100%;height:34px;background:rgba(0,0,0,.35);display:flex;align-items:center;padding:0 18px}
.brand{font-family:"Oswald",sans-serif;font-weight:700;font-size:22px;color:var(--white);letter-spacing:1px}
.main-nav{margin-left:auto;display:flex;gap:18px;align-items:center}
.main-nav a{font-size:8px;color:var(--white);text-decoration:none;text-transform:uppercase;font-weight:600}
.main-nav .call{background:var(--orange);padding:6px 10px}
.search-panel{position:absolute;left:14px;top:56px;width:158px;height:170px;background:rgba(20,20,20,.55);padding:10px 8px}
.search-panel h2{font-family:"Oswald",sans-serif;font-weight:400;font-size:15px;color:var(--white);margin-bottom:8px}
.search-panel .field{height:20px;background:var(--white);margin-bottom:8px;font-size:7px;color:var(--grey);padding:6px}
.btn{display:inline-block;background:var(--orange);color:var(--white);font-size:8px;font-weight:700;text-transform:uppercase;padding:7px 12px}
.tagline{position:absolute;right:28px;top:168px;text-align:right;font-family:"Oswald",sans-serif;font-weight:700;color:var(--white);font-size:22px;line-height:24px;text-transform:uppercase}

/* help */
.help{position:absolute;top:235px;left:0;width:100%;height:360px;text-align:center}
.help h1{margin-top:42px;font-family:"Oswald",sans-serif;font-weight:600;color:var(--orange);font-size:22px}
.help .intro{width:700px;margin:10px auto 0;font-size:7px;line-height:11px;color:var(--text)}
.contact-cards{position:absolute;top:140px;left:63px;display:flex;gap:28px}
.card{width:229px;height:122px;border:1px solid var(--light);display:flex;flex-direction:column;align-items:center;justify-content:center;font-size:7px;line-height:11px}
.card svg{display:block;margin-bottom:8px}
.card strong{display:block;color:var(--orange);font-size:9px;line-height:13px;margin-top:2px}

/* form */
.request{position:absolute;top:595px;left:0;width:100%;height:380px;background:var(--light)}
.map-shape{position:absolute;left:250px;top:40px;width:420px;height:280px;background:radial-gradient(ellipse,#dedede 0%,var(--light) 70%)}
.request h2{position:relative;text-align:center;margin-top:46px;font-family:"Oswald",sans-serif;font-weight:600;font-size:15px;color:var(--dark)}
.request-form{position:absolute;left:157px;top:90px;width:545px;display:flex;gap:14px}
.col{width:273px}
.input{height:22px;background:var(--white);border:1px solid #dcdcdc;font-size:7px;color:#999;padding:6px 8px;margin-bottom:11px}
.textarea{width:258px;height:187px;background:var(--white);border:1px solid #dcdcdc;font-size:7px;color:#999;padding:6px 8px}
.request .btn{position:absolute;left:390px;top:290px}

/* footer */
.site-footer{position:absolute;top:995px;left:0;width:100%;height:205px;background:var(--dark);color:#aaa;font-size:7px;line-height:11px;padding:52px 0 0 68px;display:flex;gap:40px}
.site-footer h3{font-family:"Open Sans",sans-serif;font-weight:700;font-size:12px;color:var(--white);margin-bottom:10px}
.about{width:340px}
.links{width:140px}
.links li{list-style:none}
.address{width:200px}
.address p+p{margin-top:10px}
</style>
</head>
<body>
<div class="page">
  <section class="hero">
    <div class="hero-photo" role="img" aria-label="Gros plan d'un mécanisme de montre de luxe aux tons orangés"></div>
    <header class="site-header">
      <div class="brand">VALORA</div>
      <nav class="main-nav">
        <a>Accueil</a><a>Qui sommes-nous</a><a>Fonctionnement</a><a>FAQ</a><a>Mon compte</a><a class="call">Call : 01 40 00 12 34</a>
      </nav>
    </header>
    <form class="search-panel">
      <h2>Nature de l'objet</h2>
      <div class="field">Montre, bijou…</div>
      <div class="field">Marque de l'objet</div>
      <div class="field">Prix estimé</div>
      <span class="btn">Rechercher</span>
    </form>
    <p class="tagline">On se lasse de tout,<br>sauf de l'argent</p>
  </section>

  <section class="help">
    <h1>BESOIN D'AIDE? NOUS SOMMES A VOTRE ECOUTE</h1>
    <p class="intro">Notre équipe d'experts est disponible pour répondre à toutes vos questions sur l'estimation de vos biens, le déroulement du prêt et la restitution de vos objets. Contactez-nous par téléphone, consultez notre foire aux questions ou écrivez-nous via le formulaire ci-dessous.</p>
    <div class="contact-cards">
      <div class="card">
        <svg width="40" height="40" viewBox="0 0 40 40"><circle cx="20" cy="20" r="19" fill="none" stroke="#b2b2b2"/><path d="M14 12c2-1 3 3 3 4s-2 1-1 3 3 4 4 4 1-2 3-1 4 1 2 4-6 0-9-3-4-9-2-11z" fill="#b2b2b2"/></svg>
        <span>Nous vous invitons à nous joindre au</span><strong>01 40 00 12 34</strong>
      </div>
      <div class="card">
        <svg width="40" height="40" viewBox="0 0 40 40"><circle cx="20" cy="20" r="19" fill="none" stroke="#b2b2b2"/><text x="20" y="27" text-anchor="middle" font-family="Oswald,sans-serif" font-size="20" fill="#b2b2b2">?</text></svg>
        <span>Nous avons aussi réponse</span><strong>Questions Fréquentes</strong>
      </div>
      <div class="card">
        <svg width="40" height="40" viewBox="0 0 40 40"><circle cx="20" cy="20" r="19" fill="none" stroke="#b2b2b2"/><rect x="11" y="14" width="18" height="12" fill="none" stroke="#b2b2b2" stroke-width="1.5"/><path d="M11 14l9 7 9-7" fill="none" stroke="#b2b2b2" stroke-width="1.5"/></svg>
        <strong>Formulaire de contact</strong><span>ou</span><strong>contact@valora-pret.fr</strong>
      </div>
    </div>
  </section>

  <section class="request">
    <div class="map-shape" role="img" aria-label="Carte du monde en filigrane"></div>
    <h2>ET EGALEMENT :</h2>
    <form class="request-form">
      <div class="col">
        <div class="input">Nom*</div>
        <div class="input">Prénom*</div>
        <div class="input">Adresse*</div>
        <div class="input">Adresse Email*</div>
        <div class="input">Numéro de Téléphone*</div>
        <div class="input">Numéro de Portable (ou de travail)</div>
      </div>
      <div class="textarea">Sujet*</div>
    </form>
    <span class="btn">Envoyer</span>
  </section>

  <footer class="site-footer">
    <div class="about">
      <h3>Vendre en vue de racheter</h3>
      <p>Confiez-nous votre objet de valeur et obtenez rapidement un prêt adapté à son estimation. Votre bien est conservé en toute sécurité dans nos coffres, assuré pendant toute la durée du contrat. À l'échéance, vous remboursez simplement le montant convenu et récupérez votre objet en parfait état, sans démarches complexes ni frais cachés.</p>
    </div>
    <ul class="links">
      <li>Accueil</li><li>Concept</li><li>Nos offres</li><li>Estimation</li><li>FAQ</li><li>Mon compte</li><li>Mentions légales</li><li>Contact</li>
    </ul>
    <div class="address">
      <p>VALORA SAS<br>12, rue des Orfèvres<br>75001 Paris, France</p>
      <p>Du lundi au vendredi de 9h à 19h<br>Tél. 01 40 00 12 34</p>
      <p>Copyright © 2015 VALORA. Tous droits réservés.</p>
    </div>
  </footer>
</div>
</body>
</html>
```